Redesign of existing website for a corporate advisory business focussed on technology

We need a redesign of our website. We are a corporate advisory business based in Sydney. Our focus is on the technology and life-science sectors. We assist our clients with capital raisings, mergers and acquisitions and other corporate transactions.

Our business is called "Harbour Ridge Partners"
Our current website is www.harbourridgeadv.com.au

I'd like to see a complete re-design of the site. (I'm happy to keep any of the existing images - but equally happy to scrap them completely and "start again".)

My preference is that the logo remain as it is. However, I would be very open to a re-colouring of the logo if it works better with a new webiste design.

The content of the website will remain the same. I'd like one additional section - "News" - which will allow us to manually post news items and which will pull in news feeds from current and past clients.

In terms of positioning / look-and-feel:

Our clients fall into two categories. I'd like the website to appeal to both:

1. The first category is: Executives from established technology or life-science companies (private or public), who engage us to assist with strategy, capital raising, corporate transactions.

2. The second category is: Entrepreneurs looking for advice in accessing angel funding or venture capital. The site should appeal to young tech-savvy entrepreneurs who are looking to engage a firm to provide such assistance.

To accomodate both target groups, the overriding feel should be one of professionalism, stability, trust and expertise. However, while the site should look fairly "corporate", I'd like it to feel contemporary and have an element of creativity and flair, reflecting the fact that our clients are often early-stage, innovative, technology companies. (I know this might be a tricky balance...)

Target Market(s)

Potential clients. Typically executives at technology or life-science companies or (more typically) entrepreneurs building their own companies

Industry/Entity Type

Business

Requirements
Must have
• 1. All content on the existing website
2. An additional section called "News" that allows us to easily add news items or articles and ideally which accepts news feeds from a handful of past and present clients
3. An ability to easily update and edit content
Should not have
• The site should not have "gimmicks". (Definitely no devices like the moving arrow in the current site!)

It should be fairly conservative, while still feeling contemporary and fresh.

```html
<!DOCTYPE html>
<html lang="en">
<head>
<meta charset="utf-8">
<title>Harbour Ridge Partners</title>
<link href="https://fonts.googleapis.com/css2?family=Noto+Sans:wght@400;700&display=swap" rel="stylesheet">
<style>
:root{
  --orange:#f58a3a;
  --orange-dark:#e8701f;
  --ink:#3a3a3a;
  --text:#4a4a4a;
  --page:#efefef;
  --panel:#f7f7f7;
  --line:#dcdcdc;
  --footer:#1f1f1f;
  --footer-deep:#0c0c0c;
  --footer-link:#c9c9c9;
}
*{box-sizing:border-box;margin:0;padding:0}
html,body{width:1024px;height:1200px;overflow:hidden}
body{position:relative;background:var(--page);font-family:"Noto Sans",sans-serif;color:var(--text)}
.abs{position:absolute}
.hero-glow{left:0;top:70px;width:1024px;height:360px;background:radial-gradient(ellipse at 45% 50%,#ffffff 0%,#f7f7f7 45%,var(--page) 75%)}
.site-header{left:96px;top:17px;width:832px;height:53px;background:linear-gradient(#fff,#f4f4f4);border-radius:6px;box-shadow:0 2px 3px rgba(0,0,0,.15)}
.brand{left:10px;top:6px;display:flex;align-items:center;gap:8px}
.brand-dot{width:42px;height:42px;border-radius:50%;background:var(--orange)}
.brand-name{font-size:15px;color:var(--ink)}
.main-nav{right:0;top:0;height:53px;display:flex}
.main-nav a{display:block;height:53px;line-height:53px;padding:0 11px;font-size:11.5px;color:#666;text-decoration:none;border-left:1px solid #e6e6e6;min-width:84px;text-align:center}
.main-nav a.current{color:var(--orange)}
.hero-title{left:142px;top:172px;color:#444;font-size:25px;line-height:1.15;letter-spacing:.5px}
.hero-title .accent{color:var(--orange);font-size:33px}
.hero-copy{left:143px;top:243px;width:352px;font-size:9.5px;line-height:1.4;color:#333}
.btn{display:inline-flex;align-items:center;gap:6px;height:24px;padding:0 8px 0 8px;border-radius:12px;background:linear-gradient(#fb9a4f,var(--orange-dark));color:#fff;font-size:9px}
.btn .chev{width:13px;height:13px;border-radius:50%;background:rgba(255,255,255,.25);display:flex;align-items:center;justify-content:center}
.hero-btn{left:141px;top:308px}
.hero-globe{left:584px;top:92px;width:276px;height:276px;border-radius:50%;background:radial-gradient(circle at 40% 30%,#cfe2fb 0%,#4a86e0 40%,#1344b3 75%,#0b2f85 100%)}
.globe-shadow{left:600px;top:350px;width:260px;height:30px;border-radius:50%;background:radial-gradient(ellipse,rgba(0,0,0,.18),rgba(0,0,0,0) 70%)}
.slider-arrows{left:472px;top:380px}
.panel{background:var(--panel);border:1px solid var(--line);border-radius:3px}
.news-panel{left:94px;top:420px;width:269px;height:359px}
.welcome-panel{left:372px;top:420px;width:558px;height:359px}
.panel-title{font-size:25px;color:#444;font-weight:400}
.news-panel .panel-title{position:absolute;left:28px;top:26px}
.news-item{left:31px;width:220px;height:62px}
.thumb{width:95px;height:62px;border:3px solid #fff;box-shadow:0 0 0 1px #ddd;background:linear-gradient(135deg,#cdd6e0,#7d8ea3)}
.news-text{left:104px;top:0;font-size:11.5px;font-weight:700;line-height:1.3;color:#444;width:110px}
.news-date{left:104px;top:49px;font-size:9px;color:var(--orange)}
.news-scroll{left:116px;top:323px;display:flex;gap:5px}
.news-scroll span{width:15px;height:15px;border-radius:50%;background:#e3e3e3;border:1px solid #ccc}
.welcome-panel .panel-title{position:absolute;left:28px;top:26px}
.welcome-lead{left:28px;top:67px;width:284px;font-size:13px;color:var(--orange);line-height:1.25;text-align:justify}
.welcome-copy{left:28px;top:109px;width:284px;font-size:9.3px;line-height:1.35;text-align:justify;color:#444}
.welcome-copy p{margin-bottom:10px}
.welcome-photo{left:335px;top:70px;width:190px;height:266px;border:3px solid #fff;box-shadow:0 0 0 1px #ddd;background:linear-gradient(#dfe4ea,#8a97a8)}
.feature{top:810px;width:268px}
.feature h3{font-weight:400;font-size:21px;color:#444;margin-bottom:6px}
.feature .icon{float:left;width:46px;height:46px;border-radius:50%;margin:0 10px 2px 2px}
.feature p{font-size:9.5px;line-height:1.45;color:#555;text-align:justify}
.feature .btn{margin-top:14px;margin-left:-2px}
.site-footer{left:0;top:980px;width:1024px;height:178px;background:var(--footer)}
.footer-col{top:24px}
.footer-col h4{font-weight:400;font-size:17px;color:#fff;margin-bottom:4px}
.footer-col ul{list-style:none}
.footer-col li{font-size:9.5px;line-height:18.8px;color:var(--footer-link);text-decoration:underline}
.footer-col li::before{content:"\25B6";font-size:6px;margin-right:4px;text-decoration:none;display:inline-block}
.newsletter{left:616px;top:22px;width:310px}
.newsletter h4{font-weight:400;font-size:17px;color:#fff;line-height:1}
.newsletter .sub{font-size:9.5px;color:#fff;margin-top:2px}
.newsletter-box{position:relative;margin-top:10px;width:306px;height:92px;background:#000;border:1px solid #333;border-radius:4px}
.email{position:absolute;left:14px;top:14px;width:278px;height:34px;border-radius:3px;background:linear-gradient(#fff,#e9e9e9);font-size:9.5px;font-style:italic;color:#555;padding:11px 16px}
.nl-btn{position:absolute;top:60px;height:20px;border-radius:10px;font-size:9.5px;line-height:20px;text-align:center;width:64px}
.nl-cancel{left:156px;background:linear-gradient(#fff,#ddd);color:#333}
.nl-submit{left:228px;background:linear-gradient(#fb9a4f,var(--orange-dark));color:#fff}
.legal{left:0;top:1158px;width:1024px;height:42px;background:var(--footer-deep);color:#fff;font-size:9.5px;line-height:42px;text-align:center;border-top:1px solid #333}
</style>
</head>
<body>
<div class="abs hero-glow"></div>

<header class="abs site-header">
  <div class="abs brand"><span class="brand-dot"></span><span class="brand-name">Harbour Ridge Partners</span></div>
  <nav class="abs main-nav">
    <a class="current" href="#">Home</a><a href="#">Our services</a><a href="#">Our team</a><a href="#">Our experience</a><a href="#">Contact us</a>
  </nav>
</header>

<h1 class="abs hero-title" style="font-weight:400">WE HAVE POWER TO IMPROVE<br>YOUR <span class="accent">BUSINESS PROCESS</span></h1>
<p class="abs hero-copy">Contrary to popular belief, Lorem Ipsum is not simply random text. It has roots in a piece of classical Latin literature from 45 BC, making it over 2000 years old. Daniel Ashcombe, a Latin professor at Westbury College in Virginia.</p>
<span class="abs btn hero-btn">Read More <span class="chev"><svg width="5" height="6"><path d="M0 0L5 3L0 6Z" fill="#fff"/></svg></span></span>

<div class="abs globe-shadow"></div>
<div class="abs hero-globe" role="img" aria-label="Glossy blue globe showing Europe and Africa"></div>
<svg class="abs slider-arrows" width="80" height="24" viewBox="0 0 80 24"><path d="M22 2L2 12L22 22Z" fill="#9a9a9a"/><path d="M60 2L80 12L60 22Z" fill="#9a9a9a"/></svg>

<section class="abs panel news-panel">
  <h2 class="panel-title">Latest News</h2>
  <div class="abs news-item" style="top:70px"><div class="thumb" role="img" aria-label="Team meeting in a conference room"></div><div class="abs news-text">Lorem Ipsum is simply dummy text.</div><div class="abs news-date">00-00-00</div></div>
  <div class="abs news-item" style="top:156px"><div class="thumb" role="img" aria-label="Business partners shaking hands"></div><div class="abs news-text">Lorem Ipsum is simply dummy text.</div><div class="abs news-date">00-00-00</div></div>
  <div class="abs news-item" style="top:241px"><div class="thumb" role="img" aria-label="Office team celebrating a success"></div><div class="abs news-text">Lorem Ipsum is simply dummy text.</div><div class="abs news-date">00-00-00</div></div>
  <div class="abs news-scroll"><span></span><span></span></div>
</section>

<section class="abs panel welcome-panel">
  <h2 class="panel-title">Welcome to Harbour Ridge Partners!</h2>
  <p class="abs welcome-lead">A corporate advisory firm with a focus on life-science and technology</p>
  <div class="abs welcome-copy">
    <p>Harbour Ridge Partners is a specialist corporate advisory and investment firm with a focus on high growth companies in the Australian life-science and technology sectors.</p>
    <p>Our team combines extensive investment banking and funds management experience with sector expertise and longstanding investor relationships.</p>
    <p>Our advisory work incorporates both equity capital markets as well as mergers and acquisitions. Via our alliance with specialist US investment bank Calloway Partners LLC, we are well placed to introduce qualified international partnering opportunities to our domestic clients and to provide seamless cross-border transaction execution capabilities.</p>
    <p>Our objective is to partner with our clients over the long term, providing a skilled outsourced corporate capability to help plan, evaluate and execute significant transactions.</p>
  </div>
  <div class="abs welcome-photo" role="img" aria-label="Business figures climbing rising columns in front of a world map"></div>
</section>

<article class="abs feature" style="left:103px">
  <h3>24/7 Support</h3>
  <div class="icon" role="img" aria-label="Yellow clock icon" style="background:radial-gradient(circle,#fff 45%,#f6b81c 50%)"></div>
  <p>Lorem Ipsum is simply dummy text of the printing and typesetting industry. Lorem Ipsum has been the industry's standard, dummy text ever since the 1500s, when an unknown printer took a galley of type.</p>
  <span class="btn">Read More <span class="chev"><svg width="5" height="6"><path d="M0 0L5 3L0 6Z" fill="#fff"/></svg></span></span>
</article>
<article class="abs feature" style="left:389px">
  <h3>Global Solutions</h3>
  <div class="icon" role="img" aria-label="Small globe icon" style="background:radial-gradient(circle at 40% 35%,#8fd06a,#2b7fd0 60%,#15508f)"></div>
  <p>Lorem Ipsum is simply dummy text of the printing and typesetting industry. Lorem Ipsum has been the industry's standard, dummy text ever since the 1500s, when an unknown printer took a galley of type.</p>
  <span class="btn">Read More <span class="chev"><svg width="5" height="6"><path d="M0 0L5 3L0 6Z" fill="#fff"/></svg></span></span>
</article>
<article class="abs feature" style="left:674px">
  <h3>Growing Stategies</h3>
  <div class="icon" role="img" aria-label="Green seedling icon" style="background:radial-gradient(circle,#9fd65a,#5aa72a 70%,rgba(239,239,239,0) 72%)"></div>
  <p>Lorem Ipsum is simply dummy text of the printing and typesetting industry. Lorem Ipsum has been the industry's standard, dummy text ever since the 1500s, when an unknown printer took a galley of type.</p>
  <span class="btn">Read More <span class="chev"><svg width="5" height="6"><path d="M0 0L5 3L0 6Z" fill="#fff"/></svg></span></span>
</article>

<footer class="abs site-footer">
  <div class="abs footer-col" style="left:100px"><h4>Services</h4><ul><li>Lorem Ipsum</li><li>Dummy text</li><li>Standard dummy</li><li>Essentially unchanged</li><li>Lorem Ipsum</li><li>Desktop publishing</li></ul></div>
  <div class="abs footer-col" style="left:277px"><h4>Partners</h4><ul><li>Lorem Ipsum</li><li>Dummy text</li><li>Standard dummy</li><li>Essentially unchanged</li><li>Lorem Ipsum</li><li>Desktop publishing</li></ul></div>
  <div class="abs footer-col" style="left:456px"><h4>Archives</h4><ul><li>January 2012</li><li>Fabruary 2012</li><li>March 2012</li><li>April 2012</li><li>May 2012</li><li>June 2012</li></ul></div>
  <div class="abs newsletter">
    <h4>Join our readers list</h4>
    <div class="sub">Subscribe to our monthly newsletter</div>
    <div class="newsletter-box">
      <div class="email">Your email address...</div>
      <div class="nl-btn nl-cancel">Cancel</div>
      <div class="nl-btn nl-submit">Submit</div>
    </div>
  </div>
</footer>
<div class="abs legal">© Harbour Ridge Partners Pty Ltd 2011, AFS License No: 512907</div>
</body>
</html>
```